Social Media Designs for Pet Insurance Website

We are seeking the following
Twitter Background and Header Image
Facebook Cover
Google Plus Cover (1080×608)

All designs must comply with platform requirements with regard to size and other requirements (such as the Facebook text regulations).

The overriding requirement is for all 3 designs to be CONSISTENT with our website which can be found at www.mellow-barn-reviews.co.uk.

We would like the five colours from the menu boxes beneath the header on our home page to be incorporated into the designs.

The photo of the dog and cat which is used in our header should be incorporated within the design.

We have attached the photo file and our logo file.

We will want to use the twitter margins to display additional information about the website which we will supply at a later stage.

You are free to amend the colours in the logo to suit the design if you wish.

All 3 designs must contain our strap line which is "Helping UK pet owners make the right pet insurance choice" and also this list
"Keep in touch
Join the discussion
Contribute your experiences"

Have just added the copy for the left hand margin on the twitter background as a new attachment to the brief.   One idea might be to display the text in boxes to mimic the menu boxes on our home page.   Just an idea though  .. very happy to see other ideas.

Reason: Unfortunately I have been called away from the office for the last couple of days so have been unable to provide the feedback etc. I have therefore decided to extend the deadline by a day.

Target Market(s)

Most importantly the designs should have the same look as feel as the website..www.mellow-barn-reviews.co.uk

Industry/Entity Type

Pet

Requirements
Must have
• See brief above
Nice to have
• See brief above
Should not have
• See brief above

```html
<!DOCTYPE html>
<html lang="en">
<head>
<meta charset="utf-8">
<title>Mellow Barn Reviews UK – Social Cover</title>
<link rel="stylesheet" href="https://fonts.googleapis.com/css2?family=Fira+Sans:wght@600;700&display=swap">
<style>
  :root {
    --brand-blue: #2a7ec6;
    --accent-orange: #f07c1c;
    --ink-black: #000000;
    --paper-white: #ffffff;
    --photo-cream: #ece4d8;
    --photo-tan: #b98a55;
    --photo-brown: #4a3524;
  }
  * { box-sizing: border-box; margin: 0; padding: 0; }
  html, body {
    width: 1200px;
    height: 676px;
    overflow: hidden;
    background: var(--paper-white);
  }
  .cover {
    position: relative;
    width: 1200px;
    height: 676px;
    background: var(--paper-white);
    font-family: "Fira Sans", Arial, sans-serif;
  }
  .top-band {
    position: absolute;
    left: 0; top: 0;
    width: 100%;
    height: 25px;
    background: var(--brand-blue);
  }
  .engagement-list {
    position: absolute;
    left: 57px;
    top: 62px;
    list-style: none;
    color: var(--accent-orange);
    font-weight: 700;
    font-size: 27px;
    line-height: 36px;
  }
  .strapline {
    position: absolute;
    left: 49px;
    top: 440px;
    color: var(--brand-blue);
    font-weight: 700;
    font-size: 21px;
    line-height: 29px;
  }
  .strapline .indent { padding-left: 15px; }
  .pets-photo {
    position: absolute;
    left: 517px;
    top: 111px;
    width: 683px;
    height: 396px;
    background:
      radial-gradient(ellipse 40% 55% at 24% 55%, var(--photo-cream) 0%, rgba(236,228,216,0) 100%),
      radial-gradient(ellipse 45% 60% at 70% 55%, var(--photo-tan) 0%, var(--photo-brown) 55%, rgba(74,53,36,0) 100%),
      linear-gradient(180deg, var(--paper-white) 0%, #f3f1ee 100%);
  }
  .footer-band {
    position: absolute;
    left: 0;
    top: 533px;
    width: 100%;
    height: 143px;
    background: var(--ink-black);
  }
  .brand-name {
    position: absolute;
    left: 58px;
    top: 31px;
    display: flex;
    align-items: center;
    gap: 16px;
    color: var(--paper-white);
    font-weight: 600;
    font-size: 33px;
    line-height: 36px;
  }
  .brand-mark {
    width: 56px;
    height: 56px;
    border-radius: 50%;
    background: var(--brand-blue);
    flex: none;
  }
  .site-address {
    position: absolute;
    right: 35px;
    top: 77px;
    color: var(--paper-white);
    font-weight: 700;
    font-size: 31px;
    line-height: 36px;
  }
</style>
</head>
<body>
  <main class="cover">
    <div class="top-band"></div>

    <ul class="engagement-list">
      <li>Keep in touch</li>
      <li>Join the discussion</li>
      <li>Contribute your experiences</li>
    </ul>

    <p class="strapline">“ Helping UK pet owners make<br><span class="indent">the right pet insurance choice”</span></p>

    <div class="pets-photo" role="img" aria-label="Photo of a Siamese kitten sitting beside a lying German Shepherd puppy on a white background"></div>

    <footer class="footer-band">
      <div class="brand-name">
        <span class="brand-mark"></span>
        <span>Mellow Barn<br>Reviews UK</span>
      </div>
      <p class="site-address">www.mellow-barn-reviews.co.uk</p>
    </footer>
  </main>
</body>
</html>
```